Redesign existing website

We would like a redesign of the website http://www.velbrisanalytics.com that creates a more modern, up to date look.

Velbris Analytics creates software for social science research and is focused on making the software user friendly and easy to use. We would like to convey seriousness, but also
a very up to date, just released look.

Feel free to modify the logo if you wish.

Target Market(s)

Academics, researchers

Industry/Entity Type

Software

Requirements
Must have
• The design should incorporate the same information as the current website.

```html
<!DOCTYPE html>
<html lang="en">
<head>
<meta charset="utf-8">
<title>Velbris Analytics</title>
<link rel="stylesheet" href="https://fonts.googleapis.com/css2?family=Arimo:ital,wght@0,400;0,700;1,400&display=swap">
<style>
:root{
  --page-bg:#ececec;
  --page-light:#f7f7f7;
  --brand-blue:#1e3a8f;
  --nav-top:#4d6fc4;
  --nav-bottom:#1c3a90;
  --nav-divider:#6f8cd4;
  --sky:#4fa6ee;
  --text-dark:#4a4a4a;
  --text-body:#3c3c3c;
  --field-border:#cfcfcf;
  --field-text:#aaaaaa;
  --white:#ffffff;
}
*{box-sizing:border-box;margin:0;padding:0}
html,body{width:1200px;height:900px;overflow:hidden}
body{
  font-family:"Arimo",Arial,sans-serif;
  background:
    radial-gradient(ellipse 700px 400px at 1100px 150px,rgba(255,255,255,.8),transparent 70%),
    linear-gradient(180deg,var(--page-bg) 0,var(--page-bg) 540px,var(--page-light) 650px,var(--white) 900px);
  position:relative;
  color:var(--text-body);
}
.brand{position:absolute;left:110px;top:40px;display:flex;align-items:center;gap:12px}
.brand-dot{width:56px;height:56px;border-radius:50%;background:var(--brand-blue)}
.brand-name{font-size:24px;font-weight:700;color:var(--brand-blue)}
.login{position:absolute;top:35px;right:110px;display:flex;gap:9px}
.login-field{
  height:31px;border:1px solid var(--field-border);border-radius:8px;
  background:linear-gradient(#fff,#f4f4f4);font:13px "Arimo",Arial,sans-serif;
  color:var(--field-text);padding:0 10px;display:flex;align-items:center;
}
.login-user{width:188px}
.login-pass{width:188px;letter-spacing:2px;font-size:14px}
.login-button{width:85px;justify-content:center;color:#8a8a8a;font-weight:700;font-size:12px;letter-spacing:0}
.tagline{position:absolute;top:93px;right:110px;font-size:18px;font-style:italic;color:var(--text-dark)}
.main-nav{
  position:absolute;left:110px;top:134px;width:980px;height:44px;border-radius:7px;
  background:linear-gradient(var(--nav-top),#3457b0 45%,var(--nav-bottom));
  box-shadow:0 3px 5px rgba(0,0,0,.2);display:flex;
}
.main-nav a{
  color:var(--white);text-decoration:none;font-size:12px;display:flex;align-items:center;justify-content:center;
  border-right:1px solid var(--nav-divider);
}
.main-nav a:nth-child(1){width:97px}
.main-nav a:nth-child(2){width:110px}
.main-nav a:nth-child(3){width:91px}
.main-nav a:nth-child(4){width:112px}
.main-nav a:nth-child(5){width:124px;border-right:none}
.hero{
  position:absolute;left:112px;top:200px;width:976px;height:430px;background:var(--white);
  border:1px solid #e2e2e2;border-radius:6px;box-shadow:0 0 6px rgba(0,0,0,.12);
}
.hero-art{
  position:absolute;left:50px;top:22px;width:395px;height:385px;border-radius:8px;
  background:radial-gradient(circle at 50% 50%,#8fd6f7,#4ba6ec 55%,#e6f3fc 80%,#fff);
  opacity:.9;
}
.hero-headline{position:absolute;left:482px;top:163px;font-size:35px;line-height:39px;color:var(--sky);font-weight:400}
.hero-arrow{
  position:absolute;top:386px;width:68px;height:62px;border-radius:50%;background:var(--white);
  box-shadow:0 0 4px rgba(0,0,0,.15);display:flex;align-items:center;justify-content:center;
}
.hero-arrow-prev{left:78px}
.hero-arrow-next{left:1054px}
.welcome{position:absolute;left:110px;top:650px;width:700px}
.welcome-title{font-size:23px;font-weight:400;color:var(--text-dark)}
.welcome-title span{color:var(--brand-blue)}
.welcome p{font-size:12px;line-height:14.5px;color:var(--text-body);margin-top:20px;margin-left:2px}
.welcome p + p{margin-top:14px;width:640px}
.release{
  position:absolute;left:903px;top:655px;width:185px;height:165px;background:var(--white);
  border:1px solid #e0e0e0;border-radius:6px;box-shadow:0 0 5px rgba(0,0,0,.12);text-align:center;padding-top:16px;
}
.release-label{font-size:14px;font-weight:700;color:var(--text-dark);line-height:17px}
.release-product{font-size:24px;font-weight:700;color:var(--brand-blue);line-height:29px;margin-top:6px;text-shadow:0 1px 2px rgba(0,0,0,.2)}
.release-link{display:block;font-size:12px;color:var(--brand-blue);text-decoration:none;margin-top:9px}
.release-icon{display:block;margin:1px auto 0}
.footer-rule{position:absolute;left:110px;top:844px;width:980px;height:16px;background:linear-gradient(#bdbdbd,#e8e8e8 2px,#f4f4f4 8px,transparent)}
.copyright{position:absolute;left:110px;top:863px;font-size:11px;color:var(--text-body)}
.footer-nav{position:absolute;right:112px;top:863px;font-size:11px;display:flex}
.footer-nav a{color:var(--text-body);text-decoration:none}
.footer-nav span{margin:0 12px}
</style>
</head>
<body>
<header>
  <div class="brand"><span class="brand-dot"></span><span class="brand-name">Velbris Analytics</span></div>
  <div class="login">
    <div class="login-field login-user">Username</div>
    <div class="login-field login-pass">●●●●●●</div>
    <div class="login-field login-button">Login</div>
  </div>
  <p class="tagline">Increasing the power and efficiency of empirical social science research</p>
  <nav class="main-nav">
    <a href="#">Home</a><a href="#">Products</a><a href="#">News</a><a href="#">About Us</a><a href="#">Contact Us</a>
  </nav>
</header>

<section class="hero">
  <div class="hero-art" role="img" aria-label="Illustration of a blue molecular lattice of glossy spheres inside a cube"></div>
  <h1 class="hero-headline">Empowering the social<br>science researcher</h1>
</section>
<div class="hero-arrow hero-arrow-prev">
  <svg width="18" height="16" viewBox="0 0 18 16"><path d="M13 1 L4 8 L13 15" fill="none" stroke="#555" stroke-width="4"/></svg>
</div>
<div class="hero-arrow hero-arrow-next">
  <svg width="18" height="16" viewBox="0 0 18 16"><path d="M5 1 L14 8 L5 15" fill="none" stroke="#555" stroke-width="4"/></svg>
</div>

<section class="welcome">
  <h2 class="welcome-title">Welcome to <span>Velbris Analytics</span></h2>
  <p>The mission of Velbris Analytics, Inc. is to produce software products that multiply the power and efficiency of empirical scientific research in the social sciences.</p>
  <p>A central goal is to expand access to complex data sources and to the advanced methods of scientific investigation needed to analyze them.</p>
</section>

<aside class="release">
  <div class="release-label">Preview Release<br>Available!</div>
  <div class="release-product">Velbris Data<br>Studio</div>
  <a class="release-link" href="#">Download Preview Release</a>
  <svg class="release-icon" width="22" height="22" viewBox="0 0 22 22">
    <defs><linearGradient id="arrowFill" x1="0" y1="0" x2="0" y2="1"><stop offset="0" stop-color="#8fd3fb"/><stop offset="1" stop-color="#1f6ee0"/></linearGradient></defs>
    <path d="M7 1 H15 V10 H21 L11 21 L1 10 H7 Z" fill="url(#arrowFill)" stroke="#1c4fa8" stroke-width="1"/>
  </svg>
</aside>

<footer>
  <div class="footer-rule"></div>
  <p class="copyright">Copyright © 2011 Velbris Analytics All Rights Reserved</p>
  <nav class="footer-nav">
    <a href="#">Home</a><span>I</span><a href="#">Products</a><span>I</span><a href="#">News</a><span>I</span><a href="#">About Us</a><span>I</span><a href="#">Contact Us</a>
  </nav>
</footer>
</body>
</html>
```